Online travel site needs edgy website design

tripvane is the first Global Business Travel Website that provides the most comprehensive destination information tailored to suit the business traveller.

It is a ‘one click solution’ that offers direct access to all aspects of business travel, including general information on the city, accommodation and transportation options, economic and financial statistics, key business and services contacts, as well as leisure activities, entertainment suggestions, and listings for any personal needs.

Much more than a travel website, tripvane.com eliminates the need to buy multiple travel books or visit scores of websites. Most importantly, it is the only website that will cover such an extensive range of destinations around the world, while also featuring cities where information is really scarce. The user-friendly and consistent format for all destinations will allow the business traveller to easily navigate through more than 100 information pages on any destination.

tripvane will be simple to navigate, intuitive, unique in design, dynamic, and content rich providing a supreme user experience during navigation of the website.

The website will initially be English and is set to expand to more languages in the future.

A beta site with back-end database has been built - and now we need an edgy state of the art graphic design to reskin it.

LOOK & FEEL

Scope
The design of the site should reflect tripvane’s corporate and user centric philosophy with the following elements:

a. tripvane corporate image and branding
b. the promotion of each city destination
c. tripvane being the starting point of travel, while also a partner during travel
d. the subtle but powerful presence of advertising and sponsorship

All the above must derive from the design outline and elements that are going to be used.

Design Guidelines

Innovative and elegant design, minimalism, simplicity that permits the offering of the required information to be delivered in line with the values of Trust, Care, Discovery & Connection.

In addition:

1. The usability, navigation and the informative character of the corporate web site should not be compromised by the design.
2. The over-segmented pages and over-crowded content per page should be avoided.
3. The design should not only guide the user in an inviting way to the information required but also to intrigue them for further navigation.
4. Advertising space should be anticipated in line with the design character and DMQ standard ad sizes.
5. The use of photos / videos should also encouraged.

Key Elements

a. Branding/Logos
Throughout the website branding should be present as a “guarantee seal” for the content accuracy. Corporate logo should be placed on every page while branding should also characterise any content element and/or tool. Appendix contains the current brand guidelines. Should additional sub-logos be required for specific sections, these should be proposed.

b. Fonts
Provided your experience on the website design you are requested to propose alternative font types and sizes always taken into consideration the inviting and user friendly character that the new website should aspire to. The font type that will be proposed must be user friendly in English typography, but also could support other languages in the future.

Given the fact that the majority of the text in the website contains information and listing, the fonts and text layout should not strain and fatigue the reader.

c. SEO
The design should be friendly towards the search engines.

d. Colours
Colour is considered as an integral part of the brand identity. Tripvane.com corporate colours are orange and grey as per the Attached document reference guide.

Different tonalities of the brand colours, or colours in general, should be proposed and applied, guided always by the above described scope of Look & Feel.

e. Section Headings
As presented above, the site’s section headings (refer Overview of the Site.) The principle is to label the content following users’ needs and mindset. However, the label space should be flexible for changes. The labels should facilitate the user to understand the content they host. This is important and should be applied especially to informative content.

Another function that Headings should perform is that of promoting the website’s content, especially when this kind of content will make the user spend more time in the website. This category of Headings should be approached in a more creative and attractive way as to intrigue users to check the content hosted.

f. Icons
Icons are considered necessary in order to provide the user extra help to guide them to reach the information they need quick n’ easy. Icons not only contribute actively to the creation of an attractive look & feel but, most importantly, facilitate navigation and speed up the users’ familiarisation with the website too.

Therefore their design should be eye-catching, comprehensive and dynamic, in accordance to the new site’s colour coding and following the latest trends as these were defined by the look & feel of smart phones.

PIXELHIVE BRIEF REQUIREMENTS
Based on the above, please provide at least two (2) approaches for the following pages – this includes colour palette in line with logo, layout, fonts.

Initial submissions can just address Deliverable 1 & 2 to fine tune design before proceeding further.

Please refer sample screenshots separately attached from raw beta site for content – available for Deliverables 2 -6.

(REFER example sites we like for their creativity: http://www.brindle-studio.example.co.uk/#Background, http://www.rotaclarafestas.example.com.br/, http://pembrookweb.example.co.uk/ )

Deliverable 1: Landing /Home page
- Access log in –
o Free Account or via Workloop/Chatterbox etc
o Membership Access – Login
- How to use the site
- Allowance for video or animation
- Destination Selection
- Blog & Social media links

Deliverable 2: Destination Landing Page / Template
This is essentially a city guide template to be used for all cities throughout the site.

This page clearly depicts the four information sections
1. General
2. Business
3. Leisure
4. Personal

Also this page should include:
- Business News Feed
- Advertising & Sponsorship Spaces (according to DMQ Standards)
- Destination Time, Weather, FX rates (LIVE feeds)
- Tips

Deliverable 3: Follow the above format but show an Internal Content Page – text only with subheadings

Deliverable 4: Follow the above format but show an Internal Content Page – text and photos

Deliverable 5: Follow the above format but show an Internal Content Page – Listing Sections such as Restaurants (this must also include filter categories)

Deliverable 6: Follow the above format but show an Internal Content Page – Top 10 Experiences – this incorporates address and contact details, photo and sub-text

Deliverable 7: The Membership Landing Page which should include:
1. Intro
2. Advertising & Sponsorship Space
3. The four sections
4. Tips Section
Updates

Hi all - just to reiterate that we are open to different approaches in the design.  We only included the existing screen shots of the beta site to provide you with an idea of the content.  We definitely don't want to see anything similar.....we want it to be edgy yet simple and easy to navigate....we want to create an outstanding user experience!  Cheers Tripvane Team

Reason: Dear Designers - We are extending the period as have not had many submissions at all and want to provide more time. If you have already submitted, we will be in touch shortly with feedback. Thanks for your understanding Tripvane Team

Reason: We would like to give everyone more time so we can find the best and most preferred design.

Target Market(s)

TARGET MARKET
tripvane is a consumer focused website, offering a wide-range of easy-to-use and interactive platforms, for informative and commercial purposes, while also providing attractive and innovative advertising real-estate for potential business partners.

The target audience can be segmented as follows:

Primary Target: Professionals travelling on Business

They require up-to-date reliable information prior and during their travel, as well as facilitation to take action. They need an online Personal Assistant.

The personal characteristics of the primary target group are: busy life, tailored solutions, reliable sources, trusting, caring, and spoiled.
 
The website will have a membership option (for a small annual fee) which will provide customized information for their demographic and preferences. Sub target groups will include:
1. Business Men 40 years
3. Business Women 40 years
5. Business People with reduced mobility

Demographic & Travelling Profile of Business Travellers

• 92% of them use the internet as a source of info
• 54% are males, 38 years old
• 80% holds a college/university degree
• 68% is travelling mainly for leisure and annually 6 times per year
• 52% reserve their ticket through the internet
• 66% is travel internationally

Secondary Targets:

Executive PA’s
Executive personal assistants who need to plan their manager’s travel and provide support information for their trip.

Professionals travelling for Leisure and Partners
They have most probably used the website for their business travel, but consider it also useful for their leisure travel. The generic website, will include enough information to cover most of the leisure needs, as well as the requirements of their partners.

Direct Business-to-Business [B2B] Targets
The direct [B2B] targeted audience includes corporations that would like to use a white label solution for their staff, by using all available destinations or a selected number depending on their global network.

Business-to-Business [B2B] Targets
The [B2B] targeted audience is an indirect audience, for which tripvane promotes its services, and a key revenue stream. The B2B audience consists mainly of a diverse range of professional organisations targeting the business traveller (airlines, hotels, travel agencies, tourism authorities, entertainment companies, services, etc.) tripvane will be targeting these organisations to advertise on the site.
 
Desired Response from Target Groups

The desired response from the consumer targets is:
a) Recurrent use of website
b) Share content/experience with friends and social networking sites
c) Interact on the website’s Blog
d) Register for newsletters and offers
e) Subscribe to Membership
f) Be exposed to commercial advertisements on the website
g) Provide feedback (in the future) for services
h) Use (in the future) online services to purchase products and services
Competition

Industry/Entity Type

Travel

Requirements
Must have
• A clean crisp and professional appearance giving a sense of Trust and Reliability.
Should not have
• It should not look like every other run of the mill travel sites - Roomly.com, Wanderpost etc

```html
<!DOCTYPE html>
<html lang="en">
<head>
<meta charset="utf-8">
<title>Tripvane – Business Travel</title>
<link href="https://fonts.googleapis.com/css2?family=Open+Sans:wght@400;600;700&display=swap" rel="stylesheet">
<style>
:root{
  --orange:#f37a1f;
  --orange-dark:#e0661a;
  --peach:#fdd7b8;
  --peach-light:#feeadb;
  --ink:#333333;
  --text:#555555;
  --muted:#8a8a8a;
  --line:#dddddd;
  --bg-soft:#f1f1f1;
  --footer:#333333;
  --footer-text:#e6e6e6;
  --footer-head:#9a9a9a;
}
*{box-sizing:border-box;margin:0;padding:0}
html,body{width:745px;height:1200px;overflow:hidden}
body{position:relative;font-family:"Open Sans",Arial,sans-serif;color:var(--text);background:#fff;font-size:9px}
.abs{position:absolute}

/* header */
.top-rule{left:0;top:0;width:745px;height:4px;background:var(--orange)}
.hero-band{left:0;top:4px;width:745px;height:334px;background:linear-gradient(#fff,#f3f3f3 70%,#ececec)}
.brand{left:80px;top:20px;display:flex;align-items:center;gap:7px}
.brand-mark{width:30px;height:30px;background:var(--ink);border-radius:3px}
.brand-name{font-size:27px;font-weight:700;color:var(--orange);letter-spacing:-.5px;line-height:30px}
.account{right:78px;top:14px;display:flex;align-items:center;gap:6px;font-size:9px;color:var(--ink)}
.account .or{color:var(--orange);font-weight:600}
.signin{background:#5b7bb8;color:#fff;font-size:7px;padding:3px 8px;border-radius:2px}
.lang{display:flex;align-items:center;gap:4px;margin-left:8px;font-weight:600;font-size:8px}
.main-nav{right:78px;top:45px;display:flex;gap:22px;font-size:9px;color:var(--ink)}
.main-nav a{color:inherit;text-decoration:none;padding-bottom:4px}
.main-nav a.active{border-bottom:2px solid var(--orange)}

/* search panel */
.search{left:80px;top:80px;width:197px;height:238px;background:linear-gradient(var(--peach-light),var(--peach));border:1px solid #f8c9a3;box-shadow:0 2px 4px rgba(0,0,0,.12);padding:14px 13px}
.search h2{font-size:14px;font-weight:400;color:var(--ink);letter-spacing:.2px}
.search p{font-size:7.5px;color:var(--orange-dark);margin-top:3px;line-height:1.4}
.field{position:relative;height:19px;background:#fff;border:1px solid #eadbd0;border-radius:2px;font-size:7.5px;color:#666;padding:4px 8px;margin-top:6px;overflow:hidden}
.field::after{content:"";position:absolute;right:0;top:0;border-top:8px solid var(--orange);border-left:8px solid transparent}
.row{display:flex;gap:12px}
.row .field{flex:1}
.checks{font-size:7px;color:#666;line-height:12px;margin-top:6px;padding-left:0}
.checks span{display:inline-block;width:7px;height:7px;border:1px solid #ccc;background:#fff;margin-right:6px;vertical-align:-1px}
.proceed{display:block;margin:13px auto 0;width:101px;height:26px;background:var(--orange);color:#fff;font-size:9px;font-weight:600;text-align:center;line-height:26px;border-radius:2px}

.slide{left:294px;top:82px;width:370px;height:238px;background:linear-gradient(160deg,#c8d4dc,#eef0f0 45%,#6c6c62);box-shadow:0 1px 4px rgba(0,0,0,.25)}
.arrow{width:33px;height:33px;border-radius:50%;background:#555;border:3px solid rgba(240,200,170,.9);display:flex;align-items:center;justify-content:center}
.arrow.light{border-color:rgba(255,255,255,.8)}

.orange-rule{left:0;top:338px;width:745px;height:3px;background:var(--orange)}

/* welcome */
.welcome{left:0;top:341px;width:745px;height:243px;background:var(--bg-soft);border-bottom:1px solid #e3e3e3}
.welcome-divider{left:440px;top:352px;width:1px;height:220px;background:#e2e2e2}
.welcome h1{left:88px;top:376px;font-size:16px;font-weight:400;color:var(--orange)}
.welcome-copy{left:88px;top:411px;width:335px;font-size:7.5px;line-height:14.4px;color:var(--text)}
.welcome-copy p+p{margin-top:7px}
.dest-photo{left:480px;top:367px;width:168px;height:168px;border-radius:50%;background:radial-gradient(circle at 40% 35%,#9fd0ea,#cfe7f1 45%,#e9dcc4 75%);border:5px solid #e8e8e8}
.dest-caption{left:440px;top:550px;width:250px;text-align:center;font-size:9px;color:var(--ink)}

/* how to use */
.how-title{left:84px;top:608px;border-left:2px solid var(--orange);padding-left:10px}
.how-title h2{font-size:14px;font-weight:400;color:var(--ink)}
.how-title p{font-size:8px;font-weight:600;color:var(--ink)}
.tabs{left:84px;top:648px;width:130px;height:120px;border:1px solid var(--line)}
.tab{height:30px;display:flex;align-items:center;gap:9px;padding-left:11px;font-size:9px;font-weight:600;color:var(--ink);background:linear-gradient(#f5f5f5,#e6e6e6);border-bottom:1px solid #d8d8d8}
.tab.active{background:var(--orange);color:#fff}
.tab-body{left:214px;top:648px;width:263px;height:120px;border:1px solid var(--line);border-left:0;padding:15px 14px}
.tab-body p{font-size:7.5px;line-height:13.6px}
.tab-body a{display:inline-block;margin-top:6px;font-size:8px;color:var(--orange);text-decoration:underline}

.member-title{left:494px;top:612px;font-size:14px;font-weight:400;color:var(--ink)}
.member{left:494px;top:648px;width:178px;height:120px;border:1px solid var(--line);border-bottom:2px solid #d4d4d4;padding:11px 8px}
.member p{font-size:7.5px;line-height:11.5px;color:var(--text)}
.input{height:17px;border:1px solid #d6d6d6;font-size:7px;color:#888;padding:3px 8px;margin-top:6px;background:#fff}
.login{display:inline-block;margin-top:8px;background:var(--orange);color:#fff;font-size:7.5px;font-weight:600;padding:3px 10px;border-radius:1px}

/* destinations */
.hot{left:0;top:796px;width:745px;height:179px;background:var(--bg-soft)}
.hot-line{left:0;top:820px;width:745px;height:1px;background:#dedede}
.hot-title{left:286px;top:808px;width:173px;text-align:center;font-size:12px;color:var(--ink);background:var(--bg-soft)}
.card{top:834px;width:137px}
.card .photo{height:84px;border:4px solid #fff;box-shadow:0 1px 2px rgba(0,0,0,.15)}
.card h3{font-size:9px;font-weight:400;color:var(--ink);margin:6px 0 0 3px}
.card p{font-size:6.5px;line-height:8px;color:var(--muted);margin-left:3px}

/* footer */
.footer{left:0;top:975px;width:745px;height:225px;background:var(--footer)}
.fcol{top:1002px}
.fcol h4{font-size:11.5px;font-weight:600;color:var(--footer-head);margin-bottom:5px}
.fcol a,.fcol span{display:block;font-size:8px;line-height:13.6px;color:var(--footer-text);text-decoration:none}
.fcol .hl{color:var(--orange)}
.social a{display:flex;align-items:center;gap:5px}
.social i{display:inline-block;width:9px;height:9px;background:#777;border-radius:1px}
.copy{left:83px;top:1153px;font-size:7.5px;color:var(--footer-text)}
.flang{left:598px;top:1150px;display:flex;align-items:center;gap:5px;font-size:9px;color:var(--footer-text)}
</style>
</head>
<body>

<div class="abs top-rule"></div>
<div class="abs hero-band"></div>

<header>
  <div class="abs brand"><span class="brand-mark"></span><span class="brand-name">tripvane</span></div>
  <div class="abs account">
    <span>Register</span><span>|</span><span>Log In</span><span class="or">or</span>
    <span class="signin">Sign in</span>
    <span class="lang">
      <svg width="14" height="14" viewBox="0 0 14 14"><circle cx="7" cy="7" r="6.5" fill="#444"/><path d="M2 5h10M2 9h10M7 .5c-3 3-3 10 0 13M7 .5c3 3 3 10 0 13" stroke="#fff" stroke-width=".8" fill="none"/></svg>
      English
    </span>
  </div>
  <nav class="abs main-nav">
    <a class="active" href="#">Home</a><a href="#">Destination</a><a href="#">Blog</a><a href="#">About Us</a><a href="#">Contact Us</a>
  </nav>
</header>

<form class="abs search">
  <h2>FIND A PLACE TO STAY</h2>
  <p>Lorem Ipsum est simplement du faux texte employé dans la sition.</p>
  <div class="field">Where do you want to go?</div>
  <div class="field">Your Business?</div>
  <div class="row"><div class="field">Check In</div><div class="field">Check Out</div></div>
  <div class="row"><div class="field">Days</div><div class="field">Range</div></div>
  <div class="row">
    <div class="field" style="flex:0 0 85px">Lorem</div>
    <div class="checks"><div><span></span>Business Class</div><div><span style="border-color:#999;text-align:center;line-height:5px;font-size:7px">✓</span>Normal</div></div>
  </div>
  <span class="proceed">PROCEED</span>
</form>

<div class="abs slide" role="img" aria-label="Photo of two business travellers shaking hands beside a private jet"></div>
<div class="abs arrow" style="left:284px;top:184px"><svg width="10" height="12"><path d="M7 1 2 6l5 5" stroke="#fff" stroke-width="2" fill="none"/></svg></div>
<div class="abs arrow" style="left:643px;top:184px"><svg width="10" height="12"><path d="M3 1l5 5-5 5" stroke="#fff" stroke-width="2" fill="none"/></svg></div>

<div class="abs orange-rule"></div>

<section>
  <div class="abs welcome"></div>
  <div class="abs welcome-divider"></div>
  <h1 class="abs" style="left:88px;top:376px;font-size:16px;font-weight:400;color:var(--orange)">Welcome to Tripvane Travel</h1>
  <div class="abs welcome-copy">
    <p>Lorem Ipsum est simplement du faux texte employé dans la sition et la misen page avant impression. Le Lorem Ipsum est le faux texte standard de l'imprimerie depuis les années 1500, quand un peintre anonyme assembla ensemble des morceaux de texte pour réaliser un livre spécimen de polices de texte.</p>
    <p>Il n'a pas fait que survivre cinq siècles, mais s'est aussi adapté à la bureautique informatique, sans que son contenu n'en soit modifié. Il a été popularisé dans les années 1960 grâce à la vente de feuilles Presstype contenant des passages du Lorem Ipsum, et, plus récemment, par son inclusion dans des applications de mise en page de texte, comme Folio Layout.</p>
  </div>
  <div class="abs dest-photo" role="img" aria-label="Photo of a traveller relaxing in a beach chair by the sea"></div>
  <div class="abs arrow light" style="left:466px;top:437px"><svg width="10" height="12"><path d="M7 1 2 6l5 5" stroke="#fff" stroke-width="2" fill="none"/></svg></div>
  <div class="abs arrow light" style="left:631px;top:437px"><svg width="10" height="12"><path d="M3 1l5 5-5 5" stroke="#fff" stroke-width="2" fill="none"/></svg></div>
  <div class="abs dest-caption">SELECT YOUR DESIRE DESTINATION</div>
</section>

<section>
  <div class="abs how-title"><h2>How to Use Us?</h2><p>Check our great services</p></div>
  <div class="abs tabs">
    <div class="tab active">
      <svg width="18" height="14" viewBox="0 0 18 14"><circle cx="12" cy="2" r="1.8" fill="#fff"/><path d="M5 6l4-2 3 3-2 4M9 4 7 9 3 13M10 11l3 2M12 7l3 1" stroke="#fff" stroke-width="1.6" fill="none"/></svg>
      Visa Service</div>
    <div class="tab">
      <svg width="22" height="10" viewBox="0 0 22 10"><path d="M1 6 21 4l-2-1H4L2 2zM8 5l4-4h2l-2 4M8 5l4 4h2l-2-4" fill="#444"/></svg>
      Flights Service</div>
    <div class="tab">
      <svg width="18" height="12" viewBox="0 0 18 12"><path d="M1 1v10M17 6v5M1 8h16" stroke="#444" stroke-width="1.8"/><rect x="2" y="4" width="4" height="3" fill="#444"/><rect x="7" y="4" width="10" height="3" fill="#444"/></svg>
      Hotel Service</div>
    <div class="tab" style="border-bottom:0">
      <svg width="14" height="14" viewBox="0 0 14 14"><path d="M2 2l10 10M12 2 2 12" stroke="#444" stroke-width="2"/></svg>
      Other Services</div>
  </div>
  <div class="abs tab-body">
    <p>Lorem Ipsum est simplement du faux texte employé dans la sition et la misen page avant impression. Le Lorem Ipsum est le faux texte standard de l'imprimerie depuis les années 1500, quand un peintre anonyme assembla ensemble des morceaux de texte pour réaliser un livre spécimen de polices</p>
    <a href="#">View Detail</a>
  </div>

  <h2 class="abs member-title">Membership Login</h2>
  <div class="abs member">
    <p>Lorem Ipsum est simplement du faux texte employé dans la sition et la misen page</p>
    <div class="input" style="margin-top:9px">email</div>
    <div class="input">password</div>
    <span class="login">Login</span>
  </div>
</section>

<section>
  <div class="abs hot"></div>
  <div class="abs hot-line"></div>
  <h2 class="abs hot-title">Our Hot Destinations</h2>
  <svg class="abs" style="left:292px;top:812px" width="8" height="12"><path d="M6 1 2 6l4 5" stroke="#bbb" stroke-width="1.3" fill="none"/></svg>
  <svg class="abs" style="left:457px;top:812px" width="8" height="12"><path d="M2 1l4 5-4 5" stroke="#bbb" stroke-width="1.3" fill="none"/></svg>

  <div class="abs card" style="left:86px"><div class="photo" role="img" aria-label="Photo of a business team walking on an airfield" style="background:linear-gradient(#cfd8e0,#3a3f48 70%,#7d8288)"></div><h3>Lorem Ipsum dolor</h3><p>Lorem Ipsum est simplement du faux texte employé dans.</p></div>
  <div class="abs card" style="left:232px"><div class="photo" role="img" aria-label="Photo of travellers beside a private jet at sunset" style="background:linear-gradient(#c9b7a3,#6b5a4c 60%,#2f2a26)"></div><h3>Lorem Ipsum dolor</h3><p>Lorem Ipsum est simplement du faux texte employé dans.</p></div>
  <div class="abs card" style="left:376px"><div class="photo" role="img" aria-label="Photo of a businesswoman with luggage in an airport terminal" style="background:linear-gradient(#5d6d80,#b9c3cf 55%,#7e858c)"></div><h3>Lorem Ipsum dolor</h3><p>Lorem Ipsum est simplement du faux texte employé dans.</p></div>
  <div class="abs card" style="left:522px"><div class="photo" role="img" aria-label="Photo of business travellers pulling suitcases through a bright hall" style="background:linear-gradient(#e8efef,#c7d1d4 60%,#5b6066)"></div><h3>Lorem Ipsum dolor</h3><p>Lorem Ipsum est simplement du faux texte employé dans.</p></div>
</section>

<footer>
  <div class="abs footer"></div>
  <div class="abs fcol" style="left:84px"><h4>Company</h4><a>About</a><a>Contact Us</a><a>Meet Our Team</a><a>Newsroom</a><a>Blog</a><a>Privacy Policy</a><a>Terms of Use</a></div>
  <div class="abs fcol" style="left:221px"><h4>Help</h4><a>How It Works</a><a>Help Center</a><a>Getting Started</a><a>Community Guidelines</a><a>Is Home Swapping Safe?</a></div>
  <div class="abs fcol" style="left:358px"><h4>Useful Links</h4><a>Pricing &amp; Benefits</a><a>Member Stories</a><a>Travel Resources</a><a>Known Issues</a><span style="margin-top:10px">Already a Member of</span><span>Tripvane ?</span><a class="hl">Get our Special Offer!</a></div>
  <div class="abs fcol social" style="left:494px"><h4>Follow Us</h4><a><i style="background:#5b7bb8"></i>Chatterbox</a><a><i style="background:#4aa3d9"></i>Chirpline</a><a><i style="background:#d9534f"></i>Pinboardly</a><a><i></i>Orbitly +</a></div>
  <div class="abs fcol" style="left:596px"><h4>Get Started</h4><span>Not a Member yet?</span><a class="hl">Join Now!</a></div>
  <div class="abs copy">© Tripvane.com™ All Rights Reserved.</div>
  <div class="abs flang">
    <svg width="12" height="12" viewBox="0 0 14 14"><circle cx="7" cy="7" r="6" fill="none" stroke="#e6e6e6" stroke-width="1.2"/><path d="M1 7h12M7 1c-3 3-3 9 0 12M7 1c3 3 3 9 0 12" stroke="#e6e6e6" stroke-width=".9" fill="none"/></svg>
    English
  </div>
</footer>

</body>
</html>
```